Estate Agent Board Design

Most eye-catching, elegant estate agent board
Company logo should stand out
Keyvault & CPRT should be small but visible.

On the board must be:

"FOR SALE"
logos
website hkwestates.co.uk
tel number 01632 960418

It Company

```html
<!DOCTYPE html>
<html lang="en">
<head>
<meta charset="utf-8">
<title>HKW Estates Sales &amp; Lettings: For Sale Board</title>
<link href="https://fonts.googleapis.com/css2?family=Archivo+Black&family=Poppins:wght@400;600;700&display=swap" rel="stylesheet">
<style>
  :root {
    --brand-green: #1d6b1a;
    --sale-light: #6fcf2a;
    --sale-dark: #2f7f0c;
    --board-top: #f4fbe6;
    --board-bottom: #a9df6a;
    --header-white: #ffffff;
    --ink: #2b2b2b;
    --icon-blue: #1f8fd6;
    --badge-navy: #1e2f45;
    --badge-blue: #2a5fb0;
    --badge-gold: #e8c23a;
    --button-light: #7ccf2e;
    --button-dark: #2f8d10;
  }
  html, body {
    margin: 0;
    padding: 0;
    overflow: hidden;
    background: #ffffff;
  }
  .board {
    position: relative;
    width: 913px;
    height: 1200px;
    overflow: hidden;
    background: linear-gradient(180deg, var(--board-top) 0%, #d6f0ad 45%, var(--board-bottom) 100%);
    font-family: "Poppins", sans-serif;
  }
  .header {
    position: absolute;
    left: 0; top: 0;
    width: 913px; height: 240px;
  }
  .brand {
    position: absolute;
    top: 38px;
    left: 0; right: 0;
    display: flex;
    justify-content: center;
    align-items: center;
    gap: 20px;
  }
  .brand-dot {
    width: 62px; height: 62px;
    border-radius: 50%;
    background: var(--brand-green);
    flex: none;
  }
  .brand-text {
    display: flex;
    flex-direction: column;
    align-items: flex-start;
  }
  .brand-name {
    font-family: "Poppins", sans-serif;
    font-weight: 700;
    font-size: 68px;
    line-height: 1;
    color: var(--brand-green);
    letter-spacing: 1px;
  }
  .brand-tagline {
    font-family: "Poppins", sans-serif;
    font-weight: 600;
    font-size: 22px;
    line-height: 1;
    color: var(--brand-green);
    letter-spacing: 6px;
    margin-top: 10px;
  }
  .headline {
    position: absolute;
    margin: 0;
    font-family: "Archivo Black", sans-serif;
    font-size: 232px;
    line-height: 1;
    letter-spacing: 4px;
    background: linear-gradient(180deg, var(--sale-light) 0%, #4aa81a 55%, var(--sale-dark) 100%);
    -webkit-background-clip: text;
    background-clip: text;
    color: transparent;
    filter: drop-shadow(4px 6px 4px rgba(0,0,0,0.35));
  }
  .headline-for { top: 290px; left: 92px; }
  .headline-sale { top: 510px; left: 150px; }
  .contacts {
    position: absolute;
    left: 168px;
    top: 805px;
    display: flex;
    flex-direction: column;
    gap: 22px;
  }
  .contact-line {
    display: flex;
    align-items: center;
    gap: 22px;
    font-size: 46px;
    color: var(--ink);
    line-height: 1;
  }
  .contact-icon { width: 56px; height: 56px; flex: none; }
  .accreditations {
    position: absolute;
    left: 52px;
    top: 1010px;
    display: flex;
    gap: 34px;
  }
  .read-more {
    position: absolute;
    left: 505px;
    top: 1043px;
    width: 312px;
    height: 92px;
    border-radius: 46px;
    background: linear-gradient(180deg, var(--button-light) 0%, var(--button-dark) 100%);
    border: 4px solid #ffffff;
    box-sizing: border-box;
    box-shadow: 0 4px 8px rgba(0,0,0,0.35);
    color: #ffffff;
    font-weight: 700;
    font-size: 44px;
    display: flex;
    align-items: center;
    justify-content: center;
    text-shadow: 0 2px 2px rgba(0,0,0,0.35);
  }
</style>
</head>
<body>
<div class="board">
  <svg class="header" viewBox="0 0 913 240" aria-hidden="true">
    <defs>
      <filter id="header-shadow" x="-5%" y="-20%" width="110%" height="150%">
        <feDropShadow dx="0" dy="6" stdDeviation="6" flood-color="#000" flood-opacity="0.25"/>
      </filter>
    </defs>
    <path d="M0 0 H913 V185 L456 228 L0 185 Z" fill="var(--header-white)" filter="url(#header-shadow)"/>
  </svg>

  <div class="brand">
    <div class="brand-dot"></div>
    <div class="brand-text">
      <span class="brand-name">HKW ESTATES</span>
      <span class="brand-tagline">SALES &amp; LETTINGS</span>
    </div>
  </div>

  <h1 class="headline headline-for">FOR</h1>
  <p class="headline headline-sale">SALE</p>

  <div class="contacts">
    <div class="contact-line">
      <svg class="contact-icon" viewBox="0 0 56 56" aria-hidden="true">
        <circle cx="28" cy="28" r="26" fill="var(--icon-blue)"/>
        <g fill="none" stroke="#ffffff" stroke-width="3">
          <circle cx="28" cy="28" r="16"/>
          <ellipse cx="28" cy="28" rx="7" ry="16"/>
          <line x1="12" y1="28" x2="44" y2="28"/>
        </g>
      </svg>
      <span class="contact-web">www.hkwestates.co.uk</span>
    </div>
    <div class="contact-line">
      <svg class="contact-icon" viewBox="0 0 56 56" aria-hidden="true">
        <circle cx="28" cy="28" r="26" fill="var(--icon-blue)"/>
        <path d="M20 14 l6 0 l3 8 l-4 3 q3 7 10 10 l3 -4 l8 3 l0 6 q-2 3 -6 3 q-14 -2 -23 -17 q-3 -7 3 -12 Z" fill="#ffffff"/>
      </svg>
      <span class="contact-phone">01632 960418</span>
    </div>
  </div>

  <div class="accreditations">
    <svg width="120" height="140" viewBox="0 0 120 140" role="img" aria-label="Keyvault accreditation badge">
      <circle cx="60" cy="60" r="56" fill="var(--badge-navy)"/>
      <rect x="10" y="108" width="100" height="30" fill="var(--badge-navy)"/>
    </svg>
    <svg width="124" height="124" viewBox="0 0 124 124" role="img" aria-label="CPRT accreditation badge">
      <circle cx="62" cy="62" r="58" fill="var(--badge-blue)"/>
      <circle cx="62" cy="62" r="38" fill="var(--badge-gold)"/>
    </svg>
  </div>

  <div class="read-more">Read More</div>
</div>
</body>
</html>
```